Letterhead Design for Law Firm that Specializes in Property Damage Litigation

We are looking for a redesign of our letterhead. Our current letterhead lists all of our current staff members and we'd like to come up with a design that does NOT list all of the staff members so that it does not need to be updated with every newly hired employee. Must be in editable format.

We are a law firm that specializes in property damage, so we need something that is professional, yet modern. The final design should use our existing logo and should use a blue color scheme (alternate colors would be gray, black, and white).

Industry/Entity Type

Legal

Colors
0054AA
0677BA
7BADD7
CADEEF
E8F1F8

```html
<!DOCTYPE html>
<html lang="en">
<head>
<meta charset="utf-8">
<title>Harlow Brennan &amp; Vance Letterhead</title>
<link href="https://fonts.googleapis.com/css2?family=Poppins:wght@400;500&display=swap" rel="stylesheet">
<style>
  :root {
    --backdrop: #e4e5e7;
    --paper: #ffffff;
    --navy: #0b2d66;
    --brand-blue: #00336a;
    --slate: #666666;
    --ink: #13306a;
  }
  html, body {
    margin: 0;
    width: 751px;
    height: 1200px;
    overflow: hidden;
    background: var(--backdrop);
    font-family: "Poppins", sans-serif;
  }
  .letterhead {
    position: absolute;
    left: 49px;
    top: 177px;
    width: 653px;
    height: 845px;
    background: var(--paper);
    box-shadow: 6px 8px 14px rgba(0,0,0,0.25);
    overflow: hidden;
    color: var(--ink);
  }
  .corner-shapes { position: absolute; inset: 0; }
  .brand { position: absolute; left: 46px; top: 40px; }
  .brand-name {
    margin: 0;
    font-size: 16px;
    line-height: 18px;
    font-weight: 500;
    color: var(--navy);
    letter-spacing: 0.5px;
    display: flex;
    align-items: center;
    gap: 8px;
  }
  .brand-mark { width: 14px; height: 14px; background: var(--slate); flex: none; }
  .recipient { position: absolute; left: 62px; top: 216px; font-size: 13px; line-height: 22px; }
  .recipient p, .sender p { margin: 0; }
  .recipient .name, .sender .name { font-weight: 500; }
  .date { position: absolute; right: 42px; top: 238px; font-size: 13px; font-weight: 500; }
  .body-copy { position: absolute; left: 46px; width: 566px; top: 302px; font-size: 12.3px; line-height: 15.4px; }
  .body-copy p { margin: 0 0 15px; text-align: justify; text-indent: 36px; }
  .sender { position: absolute; left: 509px; top: 607px; font-size: 13px; line-height: 22px; }
  .contact-list {
    position: absolute; left: 486px; top: 742px;
    margin: 0; padding: 0; list-style: none;
    font-size: 11.5px; line-height: 21.8px;
  }
  .contact-list li { display: flex; align-items: center; gap: 17px; }
  .contact-icon { width: 10px; height: 10px; flex: none; }
</style>
</head>
<body>
<div class="letterhead">
  <svg class="corner-shapes" width="653" height="845" viewBox="0 0 653 845" aria-hidden="true">
    <polygon points="262,0 470,0 507,37 400,137" fill="var(--slate)"/>
    <polygon points="470,0 653,0 653,184" fill="var(--brand-blue)"/>
    <polygon points="154,845 257,713 389,845" fill="var(--slate)"/>
    <polygon points="0,665 182,845 0,845" fill="var(--brand-blue)"/>
  </svg>

  <header class="brand">
    <p class="brand-name"><span class="brand-mark"></span>Harlow Brennan &amp; Vance</p>
  </header>

  <div class="recipient">
    <p>To,</p>
    <p class="name">Dana Porter</p>
  </div>
  <div class="date">Date : 03.04.2023</div>

  <main class="body-copy">
    <p>Lorem ipsum dolor sit amet, consectetur adipiscing elit, sed do eiusmod tempor incididunt ut labore et dolore magna aliqua. Quis ipsum suspendisse ultrices gravida. Risus commodo viverra maecenas accumsan lacus vel facilisis.Lorem ipsum dolor sit amet, consectetur adipiscing elit, sed do eiusmod tempor incididunt ut labore et dolore magna aliqua. Quis ipsum suspendisse ultrices gravida. Risus commodo viverra maecenas accumsan lacus vel facilisis.Lorem ipsum dolor sit amet, consectetur adipiscing elit, sed do eiusmod tempor incididunt ut labore et dolore magna aliqua. Quis ipsum suspendisse ultrices gravida. Risus commodo viverra maecenas accumsan lacus vel facilisis. Lorem ipsum dolor sit amet, consectetur adipiscing elit, sed do eiusmod tempor incididunt ut labore et dolore magna aliqua. Quis ipsum suspendisse ultrices gravida. Risus commodo viverra maecenas accumsan lacus vel facilisis.</p>
    <p>Lorem ipsum dolor sit amet, consectetur adipiscing elit, sed do eiusmod tempor incididunt ut labore et dolore magna aliqua. Quis ipsum suspendisse ultrices gravida. Risus commodo viverra maecenas accumsan lacus vel facilisis.Lorem ipsum dolor sit amet, consectetur adipiscing elit, sed do eiusmod tempor incididunt ut labore et dolore magna aliqua. Quis ipsum suspendisse ultrices gravida. Risus commodo viverra maecenas accumsan lacus vel facilisis.</p>
  </main>

  <div class="sender">
    <p>From</p>
    <p class="name">Owen Reyes</p>
  </div>

  <ul class="contact-list">
    <li><svg class="contact-icon" viewBox="0 0 10 10" aria-hidden="true"><rect width="10" height="10" fill="var(--navy)"/><path d="M5 2a2 2 0 0 1 2 2c0 1.5-2 4-2 4S3 5.5 3 4a2 2 0 0 1 2-2z" fill="#fff"/></svg>Your'e Address</li>
    <li><svg class="contact-icon" viewBox="0 0 10 10" aria-hidden="true"><rect width="10" height="10" fill="var(--navy)"/><path d="M3 2.5l1.2 1.5-.6.7a4 4 0 0 0 1.7 1.7l.7-.6L7.5 7 6.8 7.8C4.6 7.6 2.4 5.4 2.2 3.2z" fill="#fff"/></svg>00001 0001 1001</li>
    <li><svg class="contact-icon" viewBox="0 0 10 10" aria-hidden="true"><rect width="10" height="10" fill="var(--navy)"/><rect x="2.5" y="4" width="5" height="3.5" fill="#fff"/><rect x="3.5" y="2.5" width="3" height="1.5" fill="#fff"/></svg>10001 10001 1001</li>
    <li><svg class="contact-icon" viewBox="0 0 10 10" aria-hidden="true"><rect width="10" height="10" fill="var(--navy)"/><circle cx="5" cy="5" r="2.6" fill="none" stroke="#fff" stroke-width="1"/><circle cx="5" cy="5" r="0.9" fill="#fff"/></svg>Your e-mail Id</li>
  </ul>
</div>
</body>
</html>
```